Property portal page designs

We are looking for some webpage designs (mock-ups) for a new property portal - Nestorix.com.

We are looking for at least 3 page designs based on the following 3 pages of Havrik:

1. Homepage design based on www.havrik.example
2. Search results page based on http://www.havrik.example/homes/
3. Full details page based on http://www.havrik.example/homedetails/B-7-Tovel-CA-48213/3917460528_hvid/ for example.

We want all three page designs to incorporate a new look and feel and colour palette for nestorix.com - examples of the logo for nestorix are attached.

The pages need to also incorporate what the rolls over will look like - especially when you roll over the properties in the search results page (page 2 above).

Hi there - i would like the design to be as close the havrik.example page designs as possible - but using the nestorix logo and colour scheme instead of the havrik.example logo and colour scheme. Again - I am looking for 3 page designs - 1. home page 2. Summary details, 3. Full details. Please also include how the roll-overs will appear (i.e. on the summary details, when you roll-over a property, the pop-up screen need to be included in the design etc). Thanks

```html
<!DOCTYPE html>
<html lang="en">
<head>
<meta charset="utf-8">
<title>Nestorix – Find your home</title>
<link rel="stylesheet" href="https://fonts.googleapis.com/css2?family=Arimo:wght@400;700&display=swap">
<style>
  :root{
    --teal:#27b295;
    --teal-dark:#1f9a80;
    --header-top:#f6f6f6;
    --header-bottom:#e6e6e6;
    --ink:#222;
    --muted:#7a7a7a;
    --body-text:#333;
    --white:#fff;
    --overlay:rgba(20,20,20,.72);
    --red:#e02020;
    --purple:#8a2be2;
    --sky:#1fa3c9;
    --grey-icon:#bfbfbf;
  }
  *{box-sizing:border-box;margin:0;padding:0}
  html,body{width:1200px;height:1000px;overflow:hidden;background:var(--white);font-family:"Arimo",Arial,sans-serif;color:var(--ink)}
  .page{position:relative;width:1200px;height:1000px;overflow:hidden}

  .site-header{position:absolute;left:0;top:0;width:1200px;height:77px;background:linear-gradient(var(--header-top),var(--header-bottom));box-shadow:0 2px 4px rgba(0,0,0,.15);z-index:3}
  .brand{position:absolute;left:110px;top:29px;font-size:14px;line-height:18px;color:var(--teal);font-weight:700;white-space:nowrap}
  .main-nav{position:absolute;left:0;top:30px;font-size:13px;line-height:16px;color:var(--ink)}
  .main-nav span{position:absolute;top:0;white-space:nowrap}
  .main-nav .more{display:flex;align-items:center;gap:6px}
  .account{position:absolute;left:0;top:30px;font-size:13px;line-height:16px;color:var(--ink)}
  .account > *{position:absolute;white-space:nowrap}
  .account u{text-decoration:underline}
  .help{width:20px;height:20px;border-radius:50%;background:#111;color:#fff;font-weight:700;font-size:14px;display:flex;align-items:center;justify-content:center}

  .hero{position:absolute;left:0;top:77px;width:1200px;height:541px;background:linear-gradient(180deg,#8fb4d8 0%,#c7d6e2 35%,#9a9a96 65%,#4f5c3a 100%)}
  .slide-arrow{position:absolute;top:228px}
  .slide-arrow.prev{left:40px}
  .slide-arrow.next{left:1130px}

  .search-panel{position:absolute;left:326px;top:158px;width:552px;height:208px;background:var(--overlay);border-radius:4px}
  .panel-brand{position:absolute;left:38px;top:22px;display:flex;align-items:center;gap:8px;color:var(--white);font-size:21px;font-weight:700;white-space:nowrap}
  .panel-brand-dot{width:30px;height:30px;border-radius:50%;background:var(--white)}
  .panel-title{position:absolute;left:246px;top:24px;color:var(--white);font-size:35px;line-height:40px;font-weight:700;white-space:nowrap}
  .search-tabs{position:absolute;left:38px;top:85px;color:var(--white);font-size:14px;font-weight:700}
  .search-tabs .tab{position:absolute;top:0;display:flex;align-items:center;gap:8px;white-space:nowrap}
  .search-field{position:absolute;left:35px;top:136px;width:437px;height:52px;background:var(--white);border-radius:3px 0 0 3px;padding-left:14px;display:flex;align-items:center;font-size:14px;color:#a8a8a8;white-space:nowrap}
  .search-button{position:absolute;left:472px;top:136px;width:55px;height:52px;background:var(--teal);border-radius:0 3px 3px 0;display:flex;align-items:center;justify-content:center}

  .reasons-heading{position:absolute;left:0;top:642px;width:1200px;text-align:center;color:var(--muted);font-size:27px;line-height:32px;font-weight:400}
  .reasons-sub{position:absolute;left:0;top:680px;width:1200px;text-align:center;color:var(--muted);font-size:17px;line-height:20px}

  .reason{position:absolute;top:772px;width:270px}
  .reason h3{position:absolute;top:147px;font-size:18px;line-height:22px;font-weight:400;color:var(--ink);white-space:nowrap}
  .reason p{position:absolute;left:2px;top:176px;width:250px;font-size:11.5px;line-height:21px;color:var(--body-text)}
  .reason-listings{left:155px}
  .reason-hidden{left:508px}
  .reason-values{left:822px}

  .photo-stack{position:absolute;left:0;top:0;width:216px;height:126px;background:linear-gradient(135deg,#6d8fb0,#c9b89a 50%,#5aa6c8);border:5px solid var(--white);box-shadow:0 2px 6px rgba(0,0,0,.3);transform:rotate(-3deg)}

  .listing-card{position:absolute;left:0;top:5px;width:229px;height:80px;background:var(--white);border-radius:6px;box-shadow:0 2px 8px rgba(0,0,0,.3)}
  .listing-card .thumb{position:absolute;left:7px;top:8px;width:66px;height:66px;background:linear-gradient(#b9cde0,#c8b49a 60%,#6e8d4f)}
  .listing-card .addr{position:absolute;left:82px;top:16px;font-size:14px;font-weight:700;color:#2c5a9e;white-space:nowrap}
  .listing-card .status{position:absolute;left:82px;top:35px;font-size:13px;font-weight:700;display:flex;align-items:center;gap:4px;white-space:nowrap}
  .listing-card .status i{width:8px;height:8px;border-radius:50%;background:#c62828;display:inline-block}
  .listing-card .price{position:absolute;left:89px;top:57px;font-size:12px;color:#333;white-space:nowrap}
  .card-floor{position:absolute;left:0;top:86px;width:229px;height:32px;background:linear-gradient(#eef1f4,rgba(255,255,255,0))}

  .value-map{position:absolute;left:64px;top:0;width:124px;height:124px;border-radius:50%;background:radial-gradient(circle,#8a9a7a,#55624a);border:4px solid #f0f0f0;box-shadow:0 1px 4px rgba(0,0,0,.3)}
</style>
</head>
<body>
<div class="page">

  <header class="site-header">
    <div class="brand">Nestorix</div>
    <nav class="main-nav">
      <span style="left:175px">Homes</span>
      <span style="left:239px">Rentals</span>
      <span style="left:305px">Mortgages</span>
      <span style="left:388px">Agents</span>
      <span style="left:451px">Advice</span>
      <span style="left:513px">Local</span>
      <span style="left:567px">Home Design</span>
      <span class="more" style="left:666px">More
        <svg width="10" height="6" viewBox="0 0 10 6"><path d="M0 0h10L5 6z" fill="#222"/></svg>
      </span>
    </nav>
    <div class="account">
      <span style="left:879px;top:2px">Advertise</span>
      <svg style="left:948px;top:0" width="18" height="18" viewBox="0 0 18 18"><circle cx="9" cy="5" r="4" fill="#333"/><path d="M1 18c0-5 4-7 8-7s8 2 8 7z" fill="#333"/></svg>
      <u style="left:972px;top:0">Sign in</u>
      <span style="left:1017px;top:0">or</span>
      <u style="left:1035px;top:0">Join</u>
      <span class="help" style="left:1070px;top:-1px">?</span>
    </div>
  </header>

  <section class="hero" role="img" aria-label="Large white colonial-style family home with wraparound porch, trees and blue sky">
    <svg class="slide-arrow prev" width="42" height="84" viewBox="0 0 42 84"><path d="M30 0h12L14 42l28 42H30L2 42z" fill="#fff"/></svg>
    <svg class="slide-arrow next" width="42" height="84" viewBox="0 0 42 84"><path d="M12 0H0l28 42L0 84h12l28-42z" fill="#fff"/></svg>

    <div class="search-panel">
      <div class="panel-brand"><span class="panel-brand-dot"></span>Nestorix.com</div>
      <div class="panel-title">Find your home</div>
      <div class="search-tabs">
        <div class="tab" style="left:0"><svg width="24" height="22" viewBox="0 0 24 22"><path d="M12 1L1 11h3v10h16V11h3z" fill="var(--red)" stroke="#fff" stroke-width="1.5"/></svg>For Sale</div>
        <div class="tab" style="left:128px"><svg width="24" height="22" viewBox="0 0 24 22"><path d="M12 1L1 11h3v10h16V11h3z" fill="var(--purple)" stroke="#fff" stroke-width="1.5"/></svg>For Rent</div>
        <div class="tab" style="left:257px"><svg width="24" height="22" viewBox="0 0 24 22"><path d="M12 1L1 11h3v10h16V11h3z" fill="var(--sky)" stroke="#fff" stroke-width="1.5"/></svg>Pre-market</div>
        <div class="tab" style="left:385px"><svg width="24" height="22" viewBox="0 0 24 22"><path d="M12 1L1 11h3v10h16V11h3z" fill="var(--grey-icon)" stroke="#fff" stroke-width="1.5"/></svg>Nestorix</div>
      </div>
      <div class="search-field">Search for an Adress, Neighbordhood, City or Zip</div>
      <div class="search-button">
        <svg width="32" height="32" viewBox="0 0 32 32"><circle cx="12" cy="12" r="9" fill="none" stroke="#fff" stroke-width="4"/><path d="M18.5 18.5L29 29" stroke="#fff" stroke-width="5" stroke-linecap="round"/></svg>
      </div>
    </div>
  </section>

  <h2 class="reasons-heading">Why shop for a home on Nestorix?</h2>
  <p class="reasons-sub">Here are 3 big reasons...</p>

  <article class="reason reason-listings">
    <div class="photo-stack" role="img" aria-label="Stack of three home photos including a house with a pool"></div>
    <h3>1 million more listings</h3>
    <p>Lorem Ipsum is simply dummy text of the print-ing and typesetting industry. Lorem Ipsum has been the industry's standard dummy text ever</p>
  </article>

  <article class="reason reason-hidden">
    <div class="listing-card">
      <div class="thumb" role="img" aria-label="Photo of a two-storey suburban house"></div>
      <div class="addr">1480 Fern Lane</div>
      <div class="status"><i></i>Coming Soon</div>
      <div class="price">Ashvale˚ $243,000</div>
    </div>
    <div class="card-floor"></div>
    <h3>Browse hidden inventory</h3>
    <p>Lorem Ipsum is simply dummy text of the print-ing and typesetting industry. Lorem Ipsum has been the industry's standard dummy text ever</p>
  </article>

  <article class="reason reason-values">
    <div class="value-map" role="img" aria-label="Aerial map of a neighbourhood with home value markers"></div>
    <h3>Nestorix values on all homes</h3>
    <p>Lorem Ipsum is simply dummy text of the print-ing and typesetting industry. Lorem Ipsum has been the industry's standard dummy text ever</p>
  </article>

</div>
</body>
</html>
```